Valeka Game Reserve, Namibia - 8pg evocative website

I need a new website... very visual and evocative as we are a game reserve in Namibia and want to entice people to come and stay.
We have 5 different lodges on the Valeka Reserve as well as two campsites and offer various game activities in Marubi and on our Reserve. We cater to various travelers - from luxury to camping - families to honeymooners... Each lodge, and it's unique selling points, needs to be featured, as well as the campsites. We need a gallery where our trade partners can download high res images of each of the camps. In addition, we need a strong call to action - taking people to a buying decision to make a booking. We have software that will link the site to a real time booking engine. I need max content management functionality.... and highly seo optimized as we want to grow our online booking capabilities.
As our site is used by both consumers planning a holiday, and the travel trade looking for detailed information about each lodge and room type, the site needs to address both user's information needs.
I have loaded a brief doc with some content and proposed structure - it is 8 pages. Instead of designing a page each for the camps, I suggest you only do ONE template page that can be duplicated per lodge.
Here are some lodge websites that I like - in no particular order:
http://korvana.example/ - nice clean lines and understated text
http://www.wildtrekplains.example/ - creative layout with sliced image banner for lodges and evocative images and clean space on lodge pages
http://www.tolemo-hills.example/
www.pelkovanmeer.example
http://www.brightcrestcollection.example/en/masako
http://www.cavelune.example/
This is what we have at the moment... www.valeka.example. Can you do better?
Thanks
Marit
Updates
Target Market(s)
Travelers to Namibia - from high end, middle to camping
Industry/Entity Type
Software
Coding
Coded - Design and coding required
Number of Pages Required
5+ page
Requirements
Must have
- *Lots of emotive images
- *Gallery with downloadable images
- *Strong links to book - via an online booking system, so the design just needs to incorporate a booking button and calls to action.
- *page for the reserve and what you can do there and game activities on the reserve
- *space/button where we can upload factsheets for each camp.
- *rates and special offers page is a must
- *contact and book now page
Nice to have
- * I have just received some 360 degree room and lodge images. It would be great to include those.
- * We have good Staywise ratings for each camp - would be great to have a block on each lodge page that pulls the latest reviews.
Should not have
- Not typical safari elements like "Big 5" and paw prints and porcupine quills - those design elements are a bit done in our industry

```html
<!DOCTYPE html>
<html lang="en">
<head>
<meta charset="utf-8">
<title>Valeka Game Reserve</title>
<link href="https://fonts.googleapis.com/css2?family=Raleway:wght@400;500;600&family=Open+Sans:wght@400;600&display=swap" rel="stylesheet">
<style>
:root{
  --green:#5c9f5e;
  --green-dark:#4a8a4d;
  --green-deep:#1f3a22;
  --green-text:#3b9a3e;
  --gold-1:#c9ad62;
  --gold-2:#9c7e32;
  --olive:#9a7c2e;
  --ink:#2a2a2a;
  --body:#555;
  --footer:#efefef;
  --line:#e4e4e4;
}
*{margin:0;padding:0;box-sizing:border-box}
html,body{width:924px;height:1200px;overflow:hidden;background:#fff}
body{position:relative;font-family:"Open Sans",sans-serif;color:var(--body)}
.abs{position:absolute}
.backdrop{position:absolute;left:0;top:0;width:924px;height:200px}
.logo{left:136px;top:28px;width:130px;height:46px;display:flex;align-items:center;gap:7px;border-right:1px solid #ccc;background:#fff}
.logo-mark{width:8px;height:8px;border-radius:50%;background:#777}
.logo-name{font-family:"Raleway",sans-serif;font-weight:400;font-size:24px;color:#666;letter-spacing:1px}
.call{right:146px;top:43px;text-align:right}
.call-label{font-size:12px;color:#555}
.call-phone{font-size:15px;color:#333;display:flex;align-items:center;justify-content:flex-end;gap:5px;margin-top:1px}
.nav{left:136px;top:87px;width:648px;height:32px;background:linear-gradient(#66aa68,var(--green-dark));display:flex}
.nav a{font-family:"Raleway",sans-serif;font-weight:500;font-size:11px;color:#fff;text-decoration:none;text-transform:uppercase;display:flex;align-items:center;justify-content:center;border-right:1px solid rgba(255,255,255,.35);letter-spacing:.2px}
.nav a:last-child{border-right:0}
.hero{left:136px;top:119px;width:648px;height:304px;background:linear-gradient(180deg,#5f5e63 0%,#6f6456 38%,#8a6a3c 60%,#5a6a34 78%,#3e5226 100%)}
.hero-caption{left:136px;top:209px;width:281px;height:115px;background:rgba(60,45,30,.72);padding:22px 20px 0}
.hero-title{font-size:19px;color:#fff}
.hero-sub{font-size:12px;color:#eadb8c;margin-top:2px}
.hero-text{font-size:7.5px;line-height:12px;color:#c9bfae;margin-top:8px}
.dots{left:442px;top:407px;display:flex;gap:3px}
.dots span{width:8px;height:8px;border-radius:50%;background:#bbb}
.dots span:first-child{background:#111}
.welcome{left:136px;top:442px;width:648px;text-align:center}
.welcome h1{font-family:"Raleway",sans-serif;font-weight:400;font-size:20px;color:var(--ink)}
.welcome p{font-family:"Raleway",sans-serif;font-size:10.5px;line-height:17px;color:#555;margin:10px auto 0;width:600px}
.btn{top:528px;height:29px;width:129px;color:#fff;font-family:"Raleway",sans-serif;font-weight:500;font-size:11px;display:flex;align-items:center;justify-content:center;gap:6px;text-transform:uppercase}
.btn-book{left:331px;background:linear-gradient(var(--green-deep),#2c5030)}
.btn-more{left:464px;background:linear-gradient(#6cb36d,var(--green))}
.divider{top:597px;height:2px;background:var(--line)}
.card-img{top:631px;width:155px;height:87px}
.card-title{top:726px;font-family:"Raleway",sans-serif;font-size:11.5px;color:var(--green-text)}
.card-text{top:746px;width:156px;font-size:7.3px;line-height:12.3px;color:#555}
.card-btn{top:791px;width:65px;height:19px;background:linear-gradient(var(--gold-1),var(--gold-2));color:#fff;font-size:6.5px;font-weight:600;display:flex;align-items:center;justify-content:center;border-radius:2px}
.services{left:134px;top:882px;width:370px}
.services h2{font-family:"Raleway",sans-serif;font-weight:400;font-size:20px;color:var(--ink)}
.services .lead{font-size:8.5px;color:#555;margin-top:11px}
.services ul{list-style:none;margin-top:6px}
.services li{font-size:7.2px;color:#333;line-height:16.5px;padding-left:11px;position:relative;white-space:nowrap}
.services li:before{content:"";position:absolute;left:2px;top:5px;border-left:3px solid var(--olive);border-top:3px solid transparent;border-bottom:3px solid transparent}
.gallery-title{left:523px;top:881px;font-family:"Raleway",sans-serif;font-size:17px;color:var(--olive)}
.thumb{width:82px;height:61px}
.footer{left:0;top:1092px;width:924px;height:108px;background:var(--footer);border-top:1px solid #d8d8d8}
.f-links{left:138px;top:1118px;font-family:"Raleway",sans-serif;font-weight:600;font-size:9.5px;color:#222}
.f-copy{left:138px;top:1140px;font-size:7.5px;color:#333}
.f-social{left:138px;top:1163px;display:flex;gap:5px}
.f-social span{width:14px;height:14px;background:#333;border-radius:2px}
.f-address{left:621px;top:1118px;font-size:8.2px;line-height:13px;color:#444;font-style:normal}
</style>
</head>
<body>
<svg class="backdrop" viewBox="0 0 924 200" aria-hidden="true">
  <path d="M0 0H924V180C840 170 800 120 700 95C600 75 300 85 200 110C120 130 60 160 0 150Z" fill="#f4f4f4"/>
  <path d="M0 150C60 160 120 130 200 110C300 85 600 75 700 95C800 120 840 170 924 180" fill="none" stroke="#e6e6e6" stroke-width="2"/>
</svg>

<div class="abs logo"><span class="logo-mark"></span><span class="logo-name">Valeka</span></div>

<div class="abs call">
  <div class="call-label">Call Us for Reservation</div>
  <div class="call-phone">
    <svg width="12" height="12" viewBox="0 0 24 24" aria-hidden="true"><path fill="#5c9f5e" d="M6.6 10.8a15.2 15.2 0 006.6 6.6l2.2-2.2a1 1 0 011-.25 11.4 11.4 0 003.6.57 1 1 0 011 1V20a1 1 0 01-1 1A17 17 0 013 4a1 1 0 011-1h3.5a1 1 0 011 1 11.4 11.4 0 00.57 3.6 1 1 0 01-.25 1z"/></svg>
    +264 61 480 219
  </div>
</div>

<nav class="abs nav">
  <a href="#" style="width:88px">About Us</a>
  <a href="#" style="width:131px">Accommodations</a>
  <a href="#" style="width:115px">Online Booking</a>
  <a href="#" style="width:83px">Activities</a>
  <a href="#" style="width:139px">Rates &amp; Factsheets</a>
  <a href="#" style="width:92px">Feedback</a>
</nav>

<div class="abs hero" role="img" aria-label="Giraffes grazing on the grassland at dusk"></div>
<div class="abs hero-caption">
  <div class="hero-title">Sed metus augue convallis</div>
  <div class="hero-sub">Proin nulla arcu nonummy luctus</div>
  <div class="hero-text">Sed porta Suspendisse quam leo molestie sed luctus<br>quis feugiat in pede Fusce tellus Sed metu</div>
</div>
<div class="abs dots"><span></span><span></span><span></span><span></span></div>

<section class="abs welcome">
  <h1>Welcome to Valeka Game Reserve</h1>
  <p>Situated on the eastern border of Marubi National Park, with 34 000 hectares of wilderness to explore and 5 unique lodges to choose from. An ideal destination in your Namibian journey.</p>
</section>
<a class="abs btn btn-book">Booking Now <svg width="6" height="8" viewBox="0 0 6 8"><path d="M0 0L6 4L0 8Z" fill="#999"/></svg></a>
<a class="abs btn btn-more">Read More <svg width="6" height="8" viewBox="0 0 6 8"><path d="M0 0L6 4L0 8Z" fill="#cfe6cf"/></svg></a>

<div class="abs divider" style="left:136px;width:316px"></div>
<div class="abs divider" style="left:472px;width:308px"></div>

<div class="abs card-img" style="left:134px;background:linear-gradient(160deg,#8a9a52,#c9b48a 55%,#7d8a4a)" role="img" aria-label="Family picnic beside a tent"></div>
<div class="abs card-img" style="left:298px;background:linear-gradient(160deg,#3f5f2a,#6e8a3e 55%,#4a6a2e)" role="img" aria-label="Couple relaxing at a campsite"></div>
<div class="abs card-img" style="left:462px;background:linear-gradient(180deg,#3c5a78,#2e3c4a 60%,#6a5030)" role="img" aria-label="Friends around a campfire at night"></div>
<div class="abs card-img" style="left:626px;background:linear-gradient(180deg,#c24a2a,#e0782e 45%,#3a1a10)" role="img" aria-label="Giraffe silhouette at sunset"></div>

<div class="abs card-title" style="left:135px">Cater to various Travelers</div>
<div class="abs card-title" style="left:297px">Families to honeymooners</div>
<div class="abs card-title" style="left:461px">Accommodations</div>
<div class="abs card-title" style="left:630px">Campsites &amp; Lodge</div>

<p class="abs card-text" style="left:135px">Aascetur ridiculus mus In iaculis facilisis massa Etiam eu urna Sed porta Suspendisse quam leo molestie sed luctus qui</p>
<p class="abs card-text" style="left:297px">Aascetur ridiculus mus In iaculis facilisis massa Etiam eu urna Sed porta Suspendisse quam leo molestie sed luctus qui</p>
<p class="abs card-text" style="left:461px">Aascetur ridiculus mus In iaculis facilisis massa Etiam eu urna Sed porta Suspendisse quam leo molestie sed luctus qui</p>
<p class="abs card-text" style="left:630px">Aascetur ridiculus mus In iaculis facilisis massa Etiam eu urna Sed porta Suspendisse quam leo molestie sed luctus qui</p>

<a class="abs card-btn" style="left:135px">READ MORE</a>
<a class="abs card-btn" style="left:298px">READ MORE</a>
<a class="abs card-btn" style="left:462px">READ MORE</a>
<a class="abs card-btn" style="left:631px">READ MORE</a>

<section class="abs services">
  <h2>Accommodation &amp; Services</h2>
  <p class="lead">Donec dictum lectus non odio Cras a ante vitae enim iaculis aliquam Mauris</p>
  <ul>
    <li>Camping sites for those of you with your own camping equipment who really want to get close to nature.</li>
    <li>Bush Camp for the medium budget traveller, with bungalows and rooms, perfect for the family.</li>
    <li>Tented Camp for the more exclusive safari experience, in exquisitely styled tent.</li>
    <li>Canopy Nest Camp for an intimate wildlife experience.</li>
    <li>Kestrel Ridge luxurious lodge famous for its breathtaking sunsets over Marubi Pan.</li>
    <li>Marubi Sela for a traditional bush lodge experience.</li>
  </ul>
</section>

<div class="abs gallery-title">Photo Gallery</div>
<div class="abs thumb" style="left:525px;top:911px;background:linear-gradient(150deg,#7a6a4a,#b08a5a)" role="img" aria-label="Small antelope close-up"></div>
<div class="abs thumb" style="left:613px;top:911px;background:linear-gradient(150deg,#6a5020,#b8902e)" role="img" aria-label="Rhino in golden light"></div>
<div class="abs thumb" style="left:701px;top:911px;background:linear-gradient(150deg,#8a6a3a,#c09a62)" role="img" aria-label="Lioness resting"></div>
<div class="abs thumb" style="left:525px;top:977px;background:linear-gradient(180deg,#4a5a2a,#c8a23a 60%,#2e3a1a)" role="img" aria-label="Tree on a savanna ridge"></div>
<div class="abs thumb" style="left:613px;top:977px;background:linear-gradient(150deg,#5a6a4a,#8a8a6a)" role="img" aria-label="Oryx herd"></div>
<div class="abs thumb" style="left:701px;top:977px;background:linear-gradient(150deg,#1e3a8a,#3a5ab0)" role="img" aria-label="Bird of prey in a blue sky"></div>

<footer class="abs footer"></footer>
<div class="abs f-links">About Us&nbsp; | &nbsp;Accommodations&nbsp; | &nbsp;Online Booking&nbsp; | &nbsp;Activities&nbsp; | &nbsp;Rates &amp; Factsheets&nbsp; | &nbsp;Feedback</div>
<div class="abs f-copy">© 2015 Company Name&nbsp; All right reserved&nbsp; Term of Use</div>
<div class="abs f-social"><span></span><span></span><span></span></div>
<address class="abs f-address">
  Valeka, Valeka Private Game Reserve<br>
  Marubi National Park, Namibia<br>
  reservations@valeka.example<br>
  +264 61 480 219
</address>
</body>
</html>
```